MORVA Design

We have a 5 part framework that companies use to plot their social media strategies and digital transformation activity. We would like to display the 5 elements in a circular format (please see the attachment for our current design - we want to get a better version of that).

The five elements and their meaning can be read about here: http://quellagrove.example/morva/what-is-morva/
We would like to see designs that fit our corporate image but also maintain informality and simplicity…. Ive included another image of some of the icons we've been using and enjoying to give an understanding of the stuff we like

Target Market(s)

Corporates

Industry/Entity Type

Digital

Logo Text

Brokerage, Integration, Trust, Incentives, Leadership

Colors
0255a3

Requirements
Must have
• Must be circular in format with each element neatly labelled - PLEASE REVIEW OUR CURRENT VERSION IN THE ATTACHMENTS

```html
<!DOCTYPE html>
<html lang="en">
<head>
<meta charset="utf-8">
<title>Community Management Framework</title>
<link rel="stylesheet" href="https://fonts.googleapis.com/css2?family=Roboto+Condensed:wght@400;700&family=Open+Sans:wght@400;600;700&display=swap">
<style>
  :root {
    --bg-center: #ffffff;
    --bg-edge: #e3e3e3;
    --pink: #f2788f;
    --pink-dark: #e0546f;
    --teal: #4fc4bd;
    --teal-dark: #2fa8a1;
    --peach: #f7cfa3;
    --peach-dark: #e9b37c;
    --slate: #6d6e73;
    --slate-dark: #4a4b50;
    --mist: #c3c8d3;
    --mist-dark: #a3a9b7;
    --brand-blue: #0255a3;
    --ink: #1d1d1d;
    --body-ink: #1f1f1f;
    --letter-pink: #f1899b;
    --letter-teal: #47bdb6;
    --letter-peach: #c4906a;
    --letter-slate: #43464d;
    --letter-mist: #7e838d;
  }
  * { box-sizing: border-box; margin: 0; padding: 0; }
  html, body { width: 1200px; height: 1000px; overflow: hidden; }
  body {
    position: relative;
    background: radial-gradient(circle at 50% 50%, var(--bg-center) 0%, #f4f4f4 45%, var(--bg-edge) 100%);
    font-family: "Open Sans", Arial, sans-serif;
    color: var(--body-ink);
  }
  .framework { position: absolute; inset: 0; width: 1200px; height: 1000px; }
  .ring-label {
    font-family: "Roboto Condensed", "Arial Narrow", sans-serif;
    font-size: 34px;
    letter-spacing: 1px;
    fill: var(--ink);
  }
  .hub-title {
    font-family: "Open Sans", Arial, sans-serif;
    font-weight: 700;
    font-size: 17px;
    fill: var(--ink);
  }
  .note-letter {
    position: absolute;
    font-family: "Roboto Condensed", Arial, sans-serif;
    font-weight: 700;
    font-size: 90px;
    line-height: 1;
  }
  .note-text {
    position: absolute;
    font-size: 16.5px;
    font-weight: 600;
    line-height: 22.5px;
  }
  .note-text strong { font-weight: 700; }

  .letter--leadership { left: 48px; top: 148px; color: var(--letter-teal); }
  .text--leadership { left: 108px; top: 160px; width: 128px; }

  .letter--brokerage { left: 706px; top: 30px; color: var(--letter-pink); font-size: 96px; }
  .text--brokerage { left: 767px; top: 45px; width: 226px; }

  .letter--integration { left: 996px; top: 276px; color: var(--letter-peach); }
  .text--integration { left: 1032px; top: 288px; width: 148px; }

  .letter--incentives { left: 48px; top: 664px; color: var(--letter-slate); }
  .text--incentives { left: 82px; top: 676px; width: 142px; }

  .letter--trust { left: 962px; top: 754px; color: var(--letter-mist); }
  .text--trust { left: 1015px; top: 767px; width: 154px; }
</style>
</head>
<body>

<svg class="framework" viewBox="0 0 1200 1000" xmlns="http://www.w3.org/2000/svg">
  <defs>
    <linearGradient id="grad-pink" x1="0" y1="0" x2="1" y2="1">
      <stop offset="0" stop-color="var(--pink)"/><stop offset="1" stop-color="var(--pink-dark)"/>
    </linearGradient>
    <linearGradient id="grad-teal" x1="0" y1="0" x2="1" y2="1">
      <stop offset="0" stop-color="var(--teal)"/><stop offset="1" stop-color="var(--teal-dark)"/>
    </linearGradient>
    <linearGradient id="grad-peach" x1="0" y1="0" x2="1" y2="1">
      <stop offset="0" stop-color="var(--peach)"/><stop offset="1" stop-color="var(--peach-dark)"/>
    </linearGradient>
    <linearGradient id="grad-slate" x1="0" y1="0" x2="1" y2="1">
      <stop offset="0" stop-color="var(--slate)"/><stop offset="1" stop-color="var(--slate-dark)"/>
    </linearGradient>
    <linearGradient id="grad-mist" x1="0" y1="0" x2="1" y2="1">
      <stop offset="0" stop-color="var(--mist)"/><stop offset="1" stop-color="var(--mist-dark)"/>
    </linearGradient>
    <radialGradient id="grad-icon-well" cx="0.5" cy="0.4" r="0.6">
      <stop offset="0" stop-color="#ffffff"/><stop offset="1" stop-color="#ececec"/>
    </radialGradient>
    <filter id="soft-shadow" x="-20%" y="-20%" width="140%" height="140%">
      <feDropShadow dx="0" dy="4" stdDeviation="6" flood-color="#000" flood-opacity="0.18"/>
    </filter>

    <path id="path-brokerage" d="M503,342 A130,130 0 1 1 687,342"/>
    <path id="path-leadership" d="M413,543 A130,130 0 1 1 493,377"/>
    <path id="path-integration" d="M709,382 A130,130 0 1 1 782,551"/>
    <path id="path-incentives" d="M426,622 A130,130 0 1 0 578,726"/>
    <path id="path-trust" d="M618,724 A130,130 0 1 0 771,623"/>
  </defs>

  <g class="rings" fill="none" stroke-width="58" filter="url(#soft-shadow)">
    <use href="#path-trust" class="ring ring--trust" stroke="url(#grad-mist)"/>
    <use href="#path-incentives" class="ring ring--incentives" stroke="url(#grad-slate)"/>
    <use href="#path-leadership" class="ring ring--leadership" stroke="url(#grad-teal)"/>
    <use href="#path-brokerage" class="ring ring--brokerage" stroke="url(#grad-pink)"/>
    <use href="#path-integration" class="ring ring--integration" stroke="url(#grad-peach)"/>
  </g>

  <g class="ring-labels" dominant-baseline="central" text-anchor="middle">
    <text class="ring-label"><textPath href="#path-brokerage" startOffset="50%">BROKERAGE</textPath></text>
    <text class="ring-label"><textPath href="#path-leadership" startOffset="45%">LEADERSHIP</textPath></text>
    <text class="ring-label"><textPath href="#path-integration" startOffset="62%">INTEGRATION</textPath></text>
    <text class="ring-label"><textPath href="#path-incentives" startOffset="55%">INCENTIVES</textPath></text>
    <text class="ring-label"><textPath href="#path-trust" startOffset="50%">TRUST</textPath></text>
  </g>

  <g class="icon-wells" fill="url(#grad-icon-well)">
    <circle cx="595" cy="250" r="56" role="img" aria-label="Icon: dollar sign with scissors"/>
    <circle cx="370" cy="440" r="56" role="img" aria-label="Icon: leader connected to two team members"/>
    <circle cx="830" cy="430" r="56" role="img" aria-label="Icon: figure climbing gears with dollar sign"/>
    <circle cx="450" cy="750" r="56" role="img" aria-label="Icon: hand dropping a dollar sign"/>
    <circle cx="745" cy="750" r="56" role="img" aria-label="Icon: two people shaking hands"/>
  </g>

  <g class="hub">
    <circle cx="600" cy="540" r="82" fill="#ffffff" filter="url(#soft-shadow)"/>
    <rect x="545" y="458" width="110" height="70" rx="30" fill="var(--brand-blue)" opacity="0.85"
          role="img" aria-label="Icon: cloud with a group of people"/>
    <text class="hub-title" x="600" y="558" text-anchor="middle">Community</text>
    <text class="hub-title" x="600" y="581" text-anchor="middle">Management</text>
  </g>
</svg>

<span class="note-letter letter--leadership">L</span>
<p class="note-text text--leadership">The roll of <strong>Leadership</strong> is to visibly champion and progress the purpose and vision of the community.</p>

<span class="note-letter letter--brokerage">B</span>
<p class="note-text text--brokerage"><strong>Brokerage</strong> refers to the communication pathways that provide the foundation of exchange on which communities are built....</p>

<span class="note-letter letter--integration">I</span>
<p class="note-text text--integration"><strong>Integration</strong> is the purposeful introduction of technology into the flows of everyday life....</p>

<span class="note-letter letter--incentives">I</span>
<p class="note-text text--incentives"><strong>Incentives</strong> are the glue of community action and the triggers that direct ongoing engagement toward targeted behaviours.</p>

<span class="note-letter letter--trust">T</span>
<p class="note-text text--trust"><strong>Building trust</strong> encourages people to move from the 90% into the 9% and the 9% into the 1%.</p>

</body>
</html>
```